Corvana Wound Care Business card design

We need a business card designed around our logo which was provided. The logo of preference is the colored. Also the colors and fonts were provided.

Target Market(s)

Our Referral partners are home health agencies.

Industry/Entity Type

Healthcare

Contact Information for Business Card

Name , Phone #, Email , Title

Requirements
Nice to have
• Creativity
Should not have
• basic

```html
<!DOCTYPE html>
<html lang="en">
<head>
<meta charset="utf-8">
<title>Corvana Wound Care – Business Card</title>
<link rel="stylesheet" href="https://fonts.googleapis.com/css2?family=Montserrat:wght@700;800&family=Nunito+Sans:wght@400;600&display=swap">
<style>
  :root {
    --blue-deep: #0055b0;
    --blue-mid: #1a7ec2;
    --teal: #2ab0c4;
    --navy-button: #2a55a3;
    --brand-navy: #1e4fa3;
    --ink: #16202b;
    --muted: #6b6f75;
    --icon-teal: #2aa3b5;
    --white: #ffffff;
    --page: #ffffff;
    --deco-fill: rgba(255, 255, 255, 0.13);
    --deco-edge: rgba(255, 255, 255, 0.35);
  }
  * { box-sizing: border-box; margin: 0; padding: 0; }
  html, body {
    width: 1200px;
    height: 1137px;
    overflow: hidden;
    background: var(--page);
  }
  .card {
    position: absolute;
    overflow: hidden;
    box-shadow: 0 4px 14px rgba(0, 0, 0, 0.12);
  }
  .decor-area {
    position: absolute;
    border-radius: 18px;
    background: radial-gradient(circle at 50% 50%, var(--deco-fill) 0%, rgba(255,255,255,0.04) 75%);
    border: 1.5px solid var(--deco-edge);
  }
  /* Front */
  .card-front {
    left: 229px;
    top: 122px;
    width: 733px;
    height: 417px;
    background: linear-gradient(100deg, var(--blue-mid) 0%, #1f96c4 55%, var(--teal) 100%);
  }
  .front-decor-left  { left: 37px;  top: 76px; width: 123px; height: 128px; }
  .front-decor-right { left: 626px; top: -20px; width: 127px; height: 172px; }
  .front-panel {
    position: absolute;
    inset: 0;
  }
  .brand-front {
    position: absolute;
    left: 0;
    width: 733px;
    top: 124px;
    text-align: center;
    font-family: "Montserrat", sans-serif;
    font-weight: 700;
    font-size: 24px;
    color: var(--brand-navy);
    letter-spacing: 0.2px;
  }
  .person-name {
    position: absolute;
    left: 0;
    width: 733px;
    top: 222px;
    text-align: center;
    font-family: "Montserrat", sans-serif;
    font-weight: 800;
    font-size: 29px;
    color: var(--ink);
    letter-spacing: 0.5px;
  }
  .person-title {
    position: absolute;
    left: 0;
    width: 733px;
    top: 263px;
    text-align: center;
    font-family: "Nunito Sans", sans-serif;
    font-weight: 400;
    font-size: 23px;
    color: var(--ink);
  }
  .contact-row {
    position: absolute;
    left: 0;
    width: 733px;
    top: 313px;
    display: flex;
    justify-content: center;
    gap: 26px;
    font-family: "Nunito Sans", sans-serif;
    font-size: 22px;
    color: var(--muted);
  }
  .contact-item {
    display: flex;
    align-items: center;
    gap: 10px;
  }
  .contact-item svg { flex: none; }
  .web-bar {
    position: absolute;
    left: 172px;
    top: 366px;
    width: 391px;
    height: 51px;
    background: var(--navy-button);
    border-radius: 3px 3px 0 0;
    display: flex;
    align-items: center;
    justify-content: center;
    font-family: "Montserrat", sans-serif;
    font-weight: 700;
    font-size: 21px;
    color: var(--white);
    letter-spacing: 1.6px;
  }
  /* Back */
  .card-back {
    left: 233px;
    top: 598px;
    width: 727px;
    height: 411px;
    background: linear-gradient(90deg, var(--blue-deep) 0%, #0a78bd 45%, var(--teal) 100%);
  }
  .back-decor-top    { left: 606px; top: -20px; width: 141px; height: 138px; }
  .back-decor-bottom { left: -20px; top: 276px; width: 169px; height: 155px; }
  .back-decor-corner { left: 582px; top: 263px; width: 120px; height: 127px; }
  .brand-back {
    position: absolute;
    left: 0;
    width: 727px;
    top: 162px;
    display: flex;
    align-items: center;
    justify-content: center;
    gap: 16px;
    font-family: "Montserrat", sans-serif;
    font-weight: 700;
    font-size: 36px;
    color: var(--white);
    letter-spacing: 0.3px;
  }
  .brand-mark {
    width: 30px;
    height: 30px;
    background: var(--white);
    border-radius: 4px;
    flex: none;
  }
</style>
</head>
<body>
  <section class="card card-front">
    <div class="decor-area front-decor-left" role="img" aria-label="Decorative outline shapes"></div>
    <div class="decor-area front-decor-right" role="img" aria-label="Decorative outline shape"></div>
    <svg class="front-panel" width="733" height="417" viewBox="0 0 733 417" aria-hidden="true">
      <path fill="#ffffff" d="M13,417 V310 Q13,263 60,263 H212 V122 Q212,62 272,62 H462 Q522,62 522,122 V263 H673 Q720,263 720,310 V417 Z"/>
    </svg>
    <div class="brand-front">Corvana Wound Care</div>
    <h1 class="person-name">JANE DOE</h1>
    <p class="person-title">Title Position</p>
    <div class="contact-row">
      <span class="contact-item">
        <svg width="20" height="20" viewBox="0 0 24 24" fill="none" stroke="var(--icon-teal)" stroke-width="2" stroke-linecap="round" stroke-linejoin="round"><path d="M22 16.9v3a2 2 0 0 1-2.2 2 19.8 19.8 0 0 1-8.6-3.1 19.5 19.5 0 0 1-6-6A19.8 19.8 0 0 1 2.1 4.2 2 2 0 0 1 4.1 2h3a2 2 0 0 1 2 1.7c.1.9.4 1.8.7 2.7a2 2 0 0 1-.5 2.1L8 9.8a16 16 0 0 0 6 6l1.3-1.3a2 2 0 0 1 2.1-.4c.9.3 1.8.6 2.7.7a2 2 0 0 1 1.7 2z"/><path d="M15 2a7 7 0 0 1 7 7"/><path d="M15 6a3 3 0 0 1 3 3"/></svg>
        0815550147
      </span>
      <span class="contact-item">
        <svg width="20" height="16" viewBox="0 0 24 18" fill="none" stroke="var(--icon-teal)" stroke-width="2" stroke-linejoin="round"><rect x="1.5" y="1.5" width="21" height="15" rx="1.5"/><path d="M2 2.5l10 7.5 10-7.5"/></svg>
        info@corvana-care.com
      </span>
    </div>
    <div class="web-bar">www.corvana-care.com</div>
  </section>

  <section class="card card-back">
    <div class="decor-area back-decor-top" role="img" aria-label="Decorative outline shape"></div>
    <div class="decor-area back-decor-bottom" role="img" aria-label="Decorative outline shapes"></div>
    <div class="decor-area back-decor-corner" role="img" aria-label="Decorative outline shapes"></div>
    <div class="brand-back"><span class="brand-mark"></span>Corvana Wound Care</div>
  </section>
</body>
</html>
```